STATIONERY FOR OUR CLIENT

I have a client that is a major oilseed processor in Australia. They want a deluxe gorgeous version of their business card.
I am proposing we print the business cards in Pebblo.com VELDA versions with the coloured edging, probably in black. Their business name needs to appear on both sides whether in logo or text.
The stationery needs to be layed up to look lifelike to impress the client. Ideally full stationery including letterhead, business card, with compliments, envelopes.
We want to impress our client.
*** The design needs to communicate - quality, premium, prestige, modern, expert, wealthy, abundant, sophisticated, established.
Designs need to be not too dark, not alot of black please. Clean, modern, sophisticated, upmarket, luxury brand.
I need 3 concepts to present to client and once approved, refined to then have print ready files - and working files just in case we have to make tweaks down the track.
We also need to create a one page style guide, that includes pms colour etc.
THIS IS AN URGENT JOB
Updates

Please design less with black more with clean white possibly light grey/beige as secondary colour if you are looking for contrast. I have added some examples of cards that look nice and might help with what the client is looking for. thank you and looking forward to seeing the designs

Please ensure all designs submitted have the correct contact details of our client which is in the brief. Also please do not have any black backgrounds - if any of your design do have black backgrounds, please amend. Thank you

Target Market(s)

business customers, investors, major distributors

Industry/Entity Type

Business

Font styles to use
Sans Serif

Requirements
Must have
• must have business name on both sides. designed to be printed with pebblo.com using their VELDA business card print offering.
Should not have
• alot of black

```html
<!DOCTYPE html>
<html lang="en">
<head>
<meta charset="utf-8">
<title>Kelmar Oils &amp; BioEnergy – Business Card</title>
<link href="https://fonts.googleapis.com/css2?family=Open+Sans:wght@400;600;700&display=swap" rel="stylesheet">
<style>
  :root {
    --bg: #e9e7e2;
    --green-deep: #0a4f33;
    --green: #0e7a4c;
    --green-mid: #1f9160;
    --green-light: #4fb184;
    --ink: #5a5a5a;
    --ink-dark: #333;
    --white: #ffffff;
  }
  * { margin: 0; padding: 0; box-sizing: border-box; }
  html, body { width: 1200px; height: 784px; overflow: hidden; }
  body {
    background: var(--bg);
    font-family: "Open Sans", sans-serif;
    position: relative;
  }
  .card {
    position: absolute;
    top: 233px;
    width: 520px;
    height: 318px;
    border-radius: 3px;
    box-shadow: 0 6px 18px rgba(0,0,0,.18);
    overflow: hidden;
  }
  /* Front */
  .card-front { left: 60px; }
  .front-field {
    position: absolute; inset: 0;
    background:
      radial-gradient(ellipse at 30% 40%, rgba(255,255,255,.12), transparent 60%),
      linear-gradient(135deg, var(--green-mid) 0%, var(--green) 45%, var(--green-deep) 100%);
  }
  .front-brand {
    position: absolute; left: 0; right: 0; top: 92px;
    text-align: center; color: var(--white);
  }
  .brand-dot {
    width: 58px; height: 58px; border-radius: 50%;
    background: var(--green-light);
    margin: 0 auto 14px;
  }
  .brand-name {
    font-weight: 600; font-size: 46px; letter-spacing: 22px;
    padding-left: 22px; line-height: 1;
  }
  .brand-tagline {
    font-weight: 600; font-size: 19px; margin-top: 6px;
  }
  /* Back */
  .card-back { left: 620px; background: var(--white); }
  .holder {
    position: absolute; right: 26px; top: 24px; text-align: right;
  }
  .holder-name { color: var(--green); font-weight: 700; font-size: 17px; }
  .holder-role { color: var(--ink); font-size: 12px; }
  .back-brand {
    position: absolute; left: 34px; top: 62px; color: var(--green);
  }
  .back-brand .brand-dot { width: 34px; height: 34px; margin: 0 0 8px 60px; }
  .back-brand .brand-name { font-size: 30px; letter-spacing: 14px; padding-left: 0; }
  .back-brand .brand-tagline { font-size: 13px; margin-top: 2px; }
  .contacts {
    position: absolute; left: 34px; top: 172px;
    list-style: none; color: var(--ink); font-size: 12.5px; line-height: 17px;
  }
  .contacts li { display: flex; align-items: flex-start; gap: 7px; }
  .contacts li.gap { margin-top: 8px; }
  .contacts svg { width: 13px; height: 13px; margin-top: 2px; flex: none; fill: var(--green); }
</style>
</head>
<body>

<section class="card card-front">
  <div class="front-field" role="img" aria-label="Green field with a receding pattern of soft oval dots"></div>
  <div class="front-brand">
    <div class="brand-dot"></div>
    <div class="brand-name">KELO</div>
    <div class="brand-tagline">Kelmar Oils &amp; BioEnergy</div>
  </div>
</section>

<section class="card card-back">
  <div class="holder">
    <div class="holder-name">R.K. Malden</div>
    <div class="holder-role">Managing Director</div>
  </div>
  <div class="back-brand">
    <div class="brand-dot"></div>
    <div class="brand-name">KELO</div>
    <div class="brand-tagline">Kelmar Oils &amp; BioEnergy</div>
  </div>
  <ul class="contacts">
    <li>
      <svg viewBox="0 0 16 16"><path d="M8 1 1 7.5h2V15h4v-4h2v4h4V7.5h2z"/></svg>
      <span>Unit 7, 48 Larchmont Road<br>Ashdale VIC 3188</span>
    </li>
    <li class="gap">
      <svg viewBox="0 0 16 16"><path d="M4 1 6.5 4 5 6c1 2 3 4 5 5l2-1.5L15 12l-2 3C7 15 1 9 1 3z"/></svg>
      <span>03 9000 4721</span>
    </li>
    <li>
      <svg viewBox="0 0 16 16"><path d="M4.5 1h7v14h-7zM6 3v8h4V3z"/></svg>
      <span>0400 118 360</span>
    </li>
    <li class="gap">
      <svg viewBox="0 0 16 16"><path d="M1 3h14v10H1zm1.5 1.5L8 9l5.5-4.5z"/></svg>
      <span>kelmaroil@mailbox.com</span>
    </li>
    <li>
      <svg viewBox="0 0 16 16"><path d="M8 1a7 7 0 1 0 0 14A7 7 0 0 0 8 1zm0 1.5c1 1.2 1.6 3 1.7 4.7H6.3C6.4 5.5 7 3.7 8 2.5zM6.3 8.8h3.4C9.6 10.5 9 12.3 8 13.5c-1-1.2-1.6-3-1.7-4.7zM2.6 7.2a5.5 5.5 0 0 1 2.3-3.8A9 9 0 0 0 4.8 7.2zm0 1.6h2.2a9 9 0 0 0 .1 3.8 5.5 5.5 0 0 1-2.3-3.8zm8.6 0h2.2a5.5 5.5 0 0 1-2.3 3.8 9 9 0 0 0 .1-3.8zm0-1.6a9 9 0 0 0-.1-3.8 5.5 5.5 0 0 1 2.3 3.8z"/></svg>
      <span>www.kelmaroil.com.au</span>
    </li>
    <li>
      <svg viewBox="0 0 16 16"><rect x="2" y="2" width="12" height="12" rx="1.5"/></svg>
      <span>kelmaroil.com.au/news</span>
    </li>
  </ul>
</section>

</body>
</html>
```